Orvane Yuletide Pageant 2025

We’re looking for a designer to help refresh the visual identity of our annual Christmas show while maintaining continuity from previous years. The updated design should feel festive, and warm, with a sense of celebration and anticipation. We’d like a central graphic that can be adapted for posters, social media, and digital signage, along with supporting assets for flyers and banners.

We’re open to seasonal color palettes such as rich reds, deep greens or blues, golds, silvers, or cool winter tones, and prefer typography that’s clear and elegant. The overall look should feel familiar to returning audiences while inviting and engaging for newcomers.

Two key groups: the current attenders of our congregation and the broader community in our suburb of Rochester, NY. Our congregation is made up of families, older adults, and young professionals who value faith, community and spiritual growth. The surrounding community is a fast growing friendly and family-oriented area of young professionals and longtime families.

We’re looking for a designer to help refresh the visual identity of our annual Christmas show while maintaining continuity with the theme and tone of previous years. The updated design should feel festive, and warm, with a sense of celebration and anticipation. We’d like a central graphic that can be adapted for posters, social media, and digital signage, along with supporting assets for flyers and banners.

Target Market(s)

Two key groups: the current attenders of our congregation and the broader community in our suburb of Rochester, NY. Our congregation is made up of families, older adults, and young professionals who value faith, community and spiritual growth. The surrounding community is a fast growing friendly and family-oriented area of young professionals and long time families.

Industry/Entity Type

Non-profit. Church

Font styles to use
Serif
Decorative
Script
Other font styles liked:
• Quentin

Requirements
Must have
• Sparkle, eye catching
Should not have
• must not look identical to the uploaded versions

```html
<!DOCTYPE html>
<html lang="en">
<head>
<meta charset="utf-8">
<title>Orvane Yuletide Pageant 2025</title>
<link rel="stylesheet" href="https://fonts.googleapis.com/css2?family=Poppins:wght@400;600;700;800&family=Great+Vibes&display=swap">
<style>
  :root {
    --backdrop: #dbbb5f;
    --green-light: #0f6a24;
    --green-mid: #06401a;
    --green-deep: #011608;
    --gold-1: #ffe27a;
    --gold-2: #d9a520;
    --gold-3: #a87a0e;
    --glint: #fff6c8;
    --white: #ffffff;
    --ink-green: #0b3a12;
    --pine: #1f4a2a;
    --pine-light: #3b6b44;
    --berry: #7d1418;
  }
  * { margin: 0; padding: 0; box-sizing: border-box; }
  html, body {
    width: 1200px; height: 960px; overflow: hidden;
    background: var(--backdrop);
  }
  .banner {
    position: absolute; left: 0; top: 142px;
    width: 1200px; height: 676px; overflow: hidden;
    background:
      radial-gradient(ellipse 55% 55% at 50% 18%, var(--green-light) 0%, var(--green-mid) 45%, transparent 80%),
      linear-gradient(180deg, var(--green-mid) 0%, var(--green-deep) 100%);
    font-family: "Poppins", sans-serif;
    color: var(--white);
  }
  .sparkle-field { position: absolute; inset: 0; }

  .decor { position: absolute; }
  .decor-top-left {
    left: 0; top: 0; width: 420px; height: 270px;
    background:
      linear-gradient(150deg, var(--berry) 0%, var(--pine-light) 30%, var(--pine) 55%, rgba(31,74,42,0) 78%);
    clip-path: polygon(0 0, 100% 0, 55% 55%, 20% 100%, 0 100%);
  }
  .decor-bottom-right {
    right: 0; bottom: 0; width: 320px; height: 200px;
    background:
      linear-gradient(-30deg, var(--pine-light) 0%, var(--pine) 40%, var(--berry) 58%, rgba(31,74,42,0) 80%);
    clip-path: polygon(100% 0, 100% 100%, 0 100%, 45% 35%);
  }

  .star { position: absolute; fill: url(#starGold); }

  .host {
    position: absolute; top: 90px; left: 0; width: 100%;
    text-align: center; font-weight: 700; font-size: 25px; letter-spacing: 1.5px;
  }
  .presents {
    position: absolute; top: 130px; left: 0; width: 100%;
    text-align: center; font-weight: 400; font-size: 22px; letter-spacing: 9px;
    padding-left: 9px;
  }

  .glitter {
    background-color: var(--gold-2);
    background-image:
      radial-gradient(circle, var(--glint) 0 1px, transparent 1.6px),
      radial-gradient(circle, var(--gold-1) 0 1.4px, transparent 2px),
      radial-gradient(circle, var(--gold-3) 0 1.2px, transparent 1.8px),
      radial-gradient(circle, var(--glint) 0 0.8px, transparent 1.3px),
      linear-gradient(160deg, var(--gold-1) 0%, var(--gold-2) 40%, var(--gold-3) 65%, var(--gold-1) 100%);
    background-size: 7px 7px, 11px 9px, 5px 6px, 13px 13px, 100% 100%;
    background-position: 0 0, 3px 4px, 1px 2px, 6px 1px, 0 0;
  }
  .title-line {
    position: absolute; left: 0; right: 0; margin: 0 auto;
    width: max-content; font-weight: 800; line-height: 1;
    -webkit-background-clip: text; background-clip: text; color: transparent;
    filter: drop-shadow(0 4px 6px rgba(0,0,0,.5));
  }
  .title-top { top: 172px; font-size: 126px; letter-spacing: -1px; }
  .title-main { top: 270px; font-size: 126px; letter-spacing: -2px; }
  .title-script {
    position: absolute; top: 352px; left: 0; width: 100%;
    text-align: center; font-family: "Great Vibes", cursive; font-size: 118px;
    line-height: 1; color: var(--white);
    text-shadow: 0 3px 8px rgba(0,0,0,.55);
  }
  .flares { position: absolute; inset: 0; pointer-events: none; }

  .date-bar {
    position: absolute; left: 257px; top: 509px; width: 718px; height: 64px;
    border-radius: 8px;
    display: flex; align-items: center; justify-content: center; gap: 34px;
    color: var(--ink-green); font-weight: 700; font-size: 46px; letter-spacing: -1px;
    line-height: 1; padding-top: 4px;
  }
  .date-divider { width: 2px; height: 40px; background: var(--ink-green); margin-top: -4px; }
</style>
</head>
<body>
  <main class="banner">
    <svg class="sparkle-field" width="1200" height="676" aria-hidden="true">
      <defs>
        <linearGradient id="starGold" x1="0" y1="0" x2="1" y2="1">
          <stop offset="0" stop-color="#ffe7a0"/><stop offset=".5" stop-color="#d9a520"/><stop offset="1" stop-color="#9c700c"/>
        </linearGradient>
        <radialGradient id="bokeh"><stop offset="0" stop-color="#5dff7c" stop-opacity=".8"/><stop offset="1" stop-color="#5dff7c" stop-opacity="0"/></radialGradient>
      </defs>
      <g fill="url(#bokeh)">
        <circle cx="500" cy="45" r="8"/><circle cx="602" cy="70" r="10"/><circle cx="760" cy="82" r="7"/>
        <circle cx="957" cy="15" r="10"/><circle cx="1095" cy="88" r="7"/><circle cx="1099" cy="215" r="10"/>
        <circle cx="290" cy="238" r="8"/><circle cx="385" cy="237" r="7"/><circle cx="970" cy="246" r="8"/>
        <circle cx="100" cy="520" r="10"/><circle cx="1015" cy="380" r="8"/><circle cx="700" cy="40" r="6"/>
      </g>
      <g fill="#3fd45d" opacity=".5">
        <circle cx="180" cy="495" r="1.5"/><circle cx="1120" cy="130" r="1.5"/><circle cx="860" cy="170" r="1.5"/>
        <circle cx="330" cy="340" r="1.5"/><circle cx="240" cy="460" r="1.5"/><circle cx="1160" cy="240" r="1.5"/>
        <circle cx="420" cy="120" r="1.5"/><circle cx="900" cy="600" r="1.5"/><circle cx="140" cy="380" r="1.5"/>
        <circle cx="1050" cy="300" r="1.5"/><circle cx="620" cy="620" r="1.5"/><circle cx="330" cy="600" r="1.5"/>
      </g>
    </svg>

    <div class="decor decor-top-left" role="img" aria-label="Pine garland with a red velvet bow and warm string lights"></div>
    <div class="decor decor-bottom-right" role="img" aria-label="Pine branches with a red bauble and string lights"></div>

    <svg class="star" style="left:56px;top:255px" width="60" height="60" viewBox="0 0 24 24" aria-hidden="true"><path d="M12 1l3.2 7 7.6.7-5.8 5 1.8 7.5L12 17.3 5.2 21.2 7 13.7 1.2 8.7l7.6-.7z"/></svg>
    <svg class="star" style="left:1078px;top:455px" width="52" height="52" viewBox="0 0 24 24" aria-hidden="true"><path d="M12 1l3.2 7 7.6.7-5.8 5 1.8 7.5L12 17.3 5.2 21.2 7 13.7 1.2 8.7l7.6-.7z"/></svg>
    <svg class="star" style="left:1160px;top:432px" width="44" height="44" viewBox="0 0 24 24" aria-hidden="true"><path d="M12 1l3.2 7 7.6.7-5.8 5 1.8 7.5L12 17.3 5.2 21.2 7 13.7 1.2 8.7l7.6-.7z"/></svg>
    <svg class="star" style="left:968px;top:550px" width="40" height="40" viewBox="0 0 24 24" aria-hidden="true"><path d="M12 1l3.2 7 7.6.7-5.8 5 1.8 7.5L12 17.3 5.2 21.2 7 13.7 1.2 8.7l7.6-.7z"/></svg>

    <p class="host">BRIGHTWATER FELLOWSHIP CHURCH</p>
    <p class="presents">Presents</p>

    <h1>
      <span class="title-line title-top glitter">ORVANE</span>
      <span class="title-line title-main glitter">YULETIDE</span>
      <span class="title-script">Pageant</span>
    </h1>

    <svg class="flares" width="1200" height="676" aria-hidden="true">
      <defs>
        <radialGradient id="flareGlow"><stop offset="0" stop-color="#fffbe0"/><stop offset=".35" stop-color="#ffd76a" stop-opacity=".7"/><stop offset="1" stop-color="#ffb400" stop-opacity="0"/></radialGradient>
        <g id="flare">
          <circle r="9" fill="url(#flareGlow)"/>
          <path d="M0-26 1.4-1.4 26 0 1.4 1.4 0 26-1.4 1.4-26 0-1.4-1.4z" fill="#fff4c2"/>
        </g>
      </defs>
      <use href="#flare" x="372" y="196"/>
      <use href="#flare" x="548" y="246"/>
      <use href="#flare" x="746" y="268"/>
      <use href="#flare" x="430" y="318"/>
      <use href="#flare" x="540" y="330"/>
      <use href="#flare" x="700" y="340"/>
      <use href="#flare" x="826" y="296"/>
      <use href="#flare" x="868" y="366"/>
    </svg>

    <div class="date-bar glitter">
      <span class="date-days">DECEMBER 16–17</span>
      <span class="date-divider"></span>
      <span class="date-time">6.00PM</span>
    </div>
  </main>
</body>
</html>
```